Training Course Info Brochure

Hi there, I'm looking for a design for A4 Flyer (2-3 pages) on our new Course - Infection Control. I have included a previous brochure on our courses so the designed can see the look and feel we are looking for.

As this is about Infection Control, I would also like to see some RED in the design or wording.

The brochure will need to include quite a few industry/ government logos as well and graphics are important. I have included some (Health Care Industry workers) and am also open to other graphics.

Thanks for considering!

Target Market(s)

The Health profession and students wanting to work in the health field

Industry/Entity Type

Health Care

Font styles to use
Sans Serif

Colors
3277b5
f78f20
ffffff
ec1f27

Requirements
Must have
• Similar feel to the brochure I have included in this brief.

SOME RED lettering as we are teaching Infection Control during the COVID19 pandemic
Nice to have
• Lovely design with quite a few photos graphics

Company details:

Carrow Academy of Learning
RTO 73648
FREECALL : 1800 437 982
www.carrowlearning.edu.au
info@carrowlearning.edu.au

```html
<!DOCTYPE html>
<html lang="en">
<head>
<meta charset="utf-8">
<title>Infection Control Skill Set – Carrow Academy of Learning</title>
<link href="https://fonts.googleapis.com/css2?family=Source+Sans+3:wght@400;600&display=swap" rel="stylesheet">
<style>
  :root {
    --navy: #2c3e5c;
    --gold: #c48a2a;
    --gold-box: #c9902c;
    --red: #e8202a;
    --paper: #f3f3f5;
    --ink: #1f1f24;
    --white: #ffffff;
  }
  * { margin: 0; padding: 0; box-sizing: border-box; }
  html, body { width: 1200px; height: 860px; overflow: hidden; background: var(--paper); }
  body { font-family: "Source Sans 3", "Myriad Pro", Arial, sans-serif; color: var(--ink); }
  .brochure { position: relative; width: 1200px; height: 860px; }

  .panel { position: absolute; top: 0; height: 808px; }
  .panel--about { left: 0; width: 407px; background: var(--paper); }
  .panel--format { left: 407px; width: 386px; background: var(--navy); color: var(--white); }
  .panel--skills { left: 793px; width: 407px; background: var(--paper); }

  .photo { position: absolute; left: 0; display: block; }

  /* About panel */
  .about-title {
    position: absolute; left: 58px; top: 340px;
    font-size: 33px; font-weight: 400; line-height: 1;
    padding-bottom: 6px; border-bottom: 3px solid var(--gold);
    color: var(--navy);
  }
  .about-title .accent { color: var(--red); }
  .about-lead {
    position: absolute; left: 58px; top: 399px; width: 300px;
    color: var(--red); font-size: 15px; line-height: 18px;
  }
  .about-body { position: absolute; left: 66px; top: 446px; width: 310px; }
  .about-body p { font-size: 10.6px; line-height: 13.8px; margin-bottom: 13px; }

  /* Format panel */
  .format-box {
    position: absolute; left: 24px; top: 0; width: 248px; height: 115px;
    background: var(--gold-box); border-right: 3px solid var(--white);
    padding: 43px 0 0 12px; color: var(--navy);
    font-size: 15.5px; line-height: 19.5px;
  }
  .format-body { position: absolute; left: 36px; top: 128px; width: 320px; }
  .format-body p { font-size: 11.4px; line-height: 16.5px; margin-bottom: 11px; }
  .format-body p.tight { line-height: 14px; }
  .format-body h3 {
    color: var(--gold); font-weight: 400; font-size: 15.5px;
    margin: 14px 0 10px;
  }

  /* Skills panel */
  .skills-body { position: absolute; left: 16px; top: 256px; width: 380px; }
  .skills-body h3 {
    color: var(--red); font-weight: 400; font-size: 15.5px; line-height: 17px;
    margin: 0 0 10px 2px;
  }
  .skill-list { list-style: none; font-size: 11.5px; line-height: 19.4px; margin-bottom: 12px; }
  .skill-list li::before { content: "• "; font-size: 9px; }
  .ideal { font-size: 11.5px; line-height: 15.3px; margin: 0 0 14px 4px; }
  .setting-list { list-style: none; font-size: 11.5px; line-height: 15.2px; margin-left: 4px; }
  .setting-list li::before { content: "• "; font-size: 9px; }

  /* Footer band */
  .footer { position: absolute; left: 0; top: 808px; width: 1200px; height: 52px; background: var(--navy); border-top: 3px solid var(--gold); }
  .footer-web {
    position: absolute; left: 407px; top: 0; width: 386px; height: 49px;
    background: var(--gold); color: var(--white);
    font-size: 11.5px; text-align: center; padding-top: 6px;
  }
</style>
</head>
<body>
<div class="brochure">

  <section class="panel panel--about">
    <svg class="photo" width="407" height="316" viewBox="0 0 407 316" role="img" aria-label="Photo of a smiling dental nurse in a white uniform holding a blue folder, with a clinic scene behind">
      <defs>
        <linearGradient id="aboutPhoto" x1="0" y1="0" x2="1" y2="1">
          <stop offset="0" stop-color="#d9d6d2"/>
          <stop offset="0.55" stop-color="#ece9e6"/>
          <stop offset="1" stop-color="#9fb6cf"/>
        </linearGradient>
      </defs>
      <path d="M0 0 H407 V276 Q204 345 0 276 Z" fill="url(#aboutPhoto)"/>
      <path d="M0 276 Q204 345 407 276" fill="none" stroke="var(--gold)" stroke-width="3"/>
    </svg>
    <h1 class="about-title"><span class="accent">About this</span> course</h1>
    <h2 class="about-lead">Protect yourself and others in the community from infectious diseases</h2>
    <div class="about-body">
      <p>There is not better time than now, to formally Upskill yourself and your team with a Nationally Accredited unit of Competency in Infection Control prevention including the latest COVID19 infection control protocols (Department of Health). Fast track your skills with Carrow’s Accredited Infection Control Skill set to get you job ready or enhance your current workplace skills.</p>
      <p>The COVID19 pandemic has highlighted the important of building the capacity and understanding of the workforce to practice safe infection control procedures.</p>
      <p>This skill set will provide you with the skills and knowledge to assist in protecting yourself and others in the community from infectious diseases.</p>
      <p>You will understand how infections are spread, ways of preventing the spread of infection and how to protect yourself and others from infection.</p>
      <p>The skill set is becoming increasingly important for all Health Care Workers – and all workers are encouraged to upskill themselves today, whether you are becoming Job Ready or for your professional development in Industry.</p>
    </div>
  </section>

  <section class="panel panel--format">
    <div class="format-box">Course format<br>Online with face-to-face tutorial<br>(in person or via Linkroom)</div>
    <div class="format-body">
      <p>Our course is delivered to you online which allows you to undertaken study at your own pace. It is recommended completion occurs within a month.</p>
      <p>you have completed the Online Component of your course, you are invited into a Practical Lab Session via face to face learning;&nbsp; to practice skills and undertake a workplace simulated activity.</p>
      <p class="tight">Regional locations may be fulfilled by Linkroom technology and Carrow may also conduct on-site visits as required. Carrow also travel to regional locations throughout the year. Group training sessions are also available for corporates and workplaces.</p>
      <h3>Mentor Support and Practical Sessions</h3>
      <p>Students are welcomed to the course by a short induction by your Tutor/Mentor to start you on your way with confidence!&nbsp;&nbsp; All of Carrow’s student resources, learner materials, videos are contained in Carrow’s easy to use LMS and learning is provided online at your convenience.</p>
      <h3>Industry Recognised</h3>
      <p>Carrow’s unique program in Infection Control is supported by leading Industry bodies, and includes certification by the Department of Health, and other leading Health bodies in Australia.&nbsp; Our Unit of competency is Australian Recognised and Accredited.</p>
    </div>
    <svg class="photo" style="top:600px" width="386" height="208" viewBox="0 0 386 208" role="img" aria-label="Photo of a carer in a white uniform handing a glass of water to an elderly woman in a blue floral top">
      <defs>
        <linearGradient id="carePhoto" x1="0" y1="0" x2="1" y2="0">
          <stop offset="0" stop-color="#4f86b8"/>
          <stop offset="0.5" stop-color="#b8b4ab"/>
          <stop offset="1" stop-color="#e9e6e2"/>
        </linearGradient>
      </defs>
      <path d="M0 44 Q193 -40 386 44 V208 H0 Z" fill="url(#carePhoto)"/>
      <path d="M0 44 Q193 -40 386 44" fill="none" stroke="var(--red)" stroke-width="4"/>
    </svg>
  </section>

  <section class="panel panel--skills">
    <svg class="photo" width="407" height="256" viewBox="0 0 407 256" role="img" aria-label="Photo of a nurse in pale blue scrubs using a hand sanitiser dispenser at a clinic sink">
      <defs>
        <linearGradient id="handPhoto" x1="0" y1="0" x2="1" y2="1">
          <stop offset="0" stop-color="#c9dde3"/>
          <stop offset="0.5" stop-color="#e6eef0"/>
          <stop offset="1" stop-color="#b9c7cf"/>
        </linearGradient>
      </defs>
      <path d="M0 0 H407 V210 Q210 290 0 210 Z" fill="url(#handPhoto)"/>
      <path d="M0 210 Q210 290 407 210" fill="none" stroke="var(--gold)" stroke-width="3"/>
    </svg>
    <div class="skills-body">
      <h3>Gain these skills :</h3>
      <ul class="skill-list">
        <li>Gain Industry Certification in Hand Hygiene</li>
        <li>Gain Industry Certification in COVID19 Infection Control</li>
        <li>Gain Industry Certification in Cleaning, Disinfection and Sterilisation</li>
        <li>Using personal protective equipment safely (practical session with complimentary PPE samples)</li>
        <li>Understanding the chain of infection</li>
        <li>Identify infection hazards and assess risks</li>
        <li>How to prevent the spread and transmission of infection</li>
        <li>Maintaining a clean work environment</li>
      </ul>
      <h3>Who this course is ideal for :</h3>
      <p class="ideal">The skill set course is most suitable for anyone working the healthcare sector, or those looking to enter employment in the health fields.</p>
      <h3>This training is for care workers across all<br>health care settings, including:</h3>
      <ul class="setting-list">
        <li>Hospitals</li>
        <li>Primary care</li>
        <li>Medical practices, allied health, GP and specialist clinics</li>
        <li>Aged care (both in residential aged care facilities or with visiting carers at home, including cleaners and cooks)</li>
        <li>Disability (both in residential/shared care facilities or part-time carers in people’s homes, including cleaners and cooks)</li>
        <li>Allied health</li>
        <li>Aboriginal Community Controlled Health Services</li>
        <li>Pharmacies</li>
        <li>Dental practices, including dentists, nurses, cleaners and receptionists</li>
      </ul>
    </div>
  </section>

  <footer class="footer">
    <div class="footer-web">www.carrowlearning.edu.au</div>
  </footer>
</div>
</body>
</html>
```